Announcement for a New Trauma Therapy Group - Rack Card

I need a two-sided "rack" card that is 4x9 announcing a Women's Trauma and Loss Group. I am a licensed therapist and will be starting this support group for women who have experienced trauma of all kinds. In addition to groups, I offer individual, couples, and family counseling sessions.

I would like to see designs that are soft tones and use colors like muted blues, greens, and sand tones. The final design should communicate hope and healing as well as have a peaceful feel to it.

I would like a picture of a woman's profile from either the side or from behind her. (possibly a contemplative picture on a beach)

I am attaching a picture of myself to go alongside the bio information as well.

On One Side, I need the description of the group and contact info:

Healing the Hurting Heart
Women's Trauma & Loss Group
Led by Licensed Professional Counselor, Joy Belden Crane

10 Week Group
Cost - $35 session
Group size limited to 10 participants

Topics Include:
What is Trauma?
How Trauma Affects Us
Creating a Feeling of Safety
Managing Trauma Triggers
Importance of Self Care
Healthy vs. Unhealthy Coping
Guilt, Shame, and Blame
Victim vs. Victimized
Grieving through Loss
Anger and Forgiveness
Imagining a Better Future

For More Information, Contact:
Joy Belden Crane, LPC, LMFT
(555) 614-3928
joy@brightmeadowcare.example

On Side Two:

Life hurts and does not seem fair. So what do you do when you are faced with an event in your life that knocks you off your feet? It seems no one understands what you are feeling and no one knows just what to say. It is tempting to pull away and isolate or put up a mask and pretend everything is OK.

It is my desire you know that you are not alone! There are others who understand the feelings you are going through and offer a safe place for encouraging support. I want to invite you to embark on a courageous journey of healing where you will not only learn how to "survive" after trauma and loss, but instead, learn that you can once again "thrive"!
- Joy Belden Crane, LPC, LMFT

Joy Belden Crane is a Licensed Professional Counselor and Licensed Marriage and Family Therapist. She is the owner of Still Waters Counseling Services located in Tulsa, OK.

Joy is a trauma survivor herself and understands firsthand the unique challenges that can arise on the journey to healing.

(Include Joy's picture next to bio)

(Attach logo and business information to this side as well.)

Target Market(s)

Women who have gone through a traumatic experience or loss and are hurting emotionally

Industry/Entity Type

Counsellor

Font styles to use
Serif
Script

Colors
fbe7d2
86cfc6
cfeae6
85abd2
cfdeed

Requirements
Must have
• Joy's picture as well as her logo and contact information must be on the card.
• One side of the card should describe the group with the following description:
• "Healing the Hurting Heart"
• Women's Trauma & Loss Group
• Led by Licensed Professional Counselor, Joy Belden Crane
• 10 Week Group
• Cost - $35 session
• Group size limited to 10 participants
• Topics Include:
• What is Trauma?
• How Trauma Affects Us
• Creating a Feeling of Safety
• Managing Trauma Triggers
• Importance of Self Care
• Healthy vs. Unhealthy Coping
• Guilt, Shame, and Blame
• Victim vs. Victimized
• Grieving through Loss
• Anger and Forgiveness
• Imagining a Better Future
• For More Information, Contact:
• Joy Belden Crane, LPC, LMFT
• (555) 614-3928
• joy@brightmeadowcare.example
• On the second side, it must have this note from Joy:
• Life hurts and does not seem fair. So what do you do when you are faced with an event in your life that knocks you off your feet? It seems no one understands what you are feeling and no one knows just what to say. It is tempting to pull away and isolate or put up a mask and pretend everything is OK.
• It is my desire you know that you are not alone! There are others who understand the feelings you are going through and offer a safe place for encouraging support. I want to invite you to embark on a courageous journey of healing where you will not only learn how to "survive" after trauma and loss, but instead, learn that you can once again "thrive"!
• - Joy Belden Crane, LPC, LMFT
• Joy Belden Crane is a Licensed Professional Counselor and Licensed Marriage and Family Therapist. She is the owner of Still Waters Counseling Services located in Tulsa, OK.
• Joy is a trauma survivor herself and understands firsthand the unique challenges that can arise on the journey to healing. In addition to facilitating groups, Joy also offers individual, marriage, and family counseling.
Nice to have
• soft muted colors that are peaceful. Light blues, greens, sand colors would work well. A picture at the top of the card of either a woman or a woman's profile that is hopeful such as a woman sitting at a beach overlooking the ocean.
Should not have
• No harsh or bright bold colors. This card needs to have a peaceful feeling to it.

```html
<!DOCTYPE html>
<html lang="en">
<head>
<meta charset="utf-8">
<title>Healing the Hurting Heart – Rack Card</title>
<link href="https://fonts.googleapis.com/css2?family=Cinzel:wght@500&family=Dancing+Script:wght@600&family=Montserrat:wght@800&family=Roboto+Condensed:wght@300;400;700&display=swap" rel="stylesheet">
<style>
  :root{
    --blue:#7ea3d2;
    --blue-deep:#6c93c8;
    --teal:#86cfc6;
    --teal-text:#78cbbd;
    --teal-light:#cfeae6;
    --blue-light:#cfdeed;
    --sand:#fbe7d2;
    --green:#4f8a3f;
    --ink:#1f1f1f;
    --grey-band:#e3e4e6;
    --page:#e6e9ea;
    --white:#ffffff;
  }
  *{margin:0;padding:0;box-sizing:border-box}
  html,body{width:1200px;height:1200px;overflow:hidden}
  body{background:var(--page);font-family:"Roboto Condensed",sans-serif;position:relative}
  .card{position:absolute;top:90px;width:460px;height:1020px;overflow:hidden;background:var(--white);box-shadow:0 6px 18px rgba(0,0,0,.18)}
  .card--front{left:100px}
  .card--back{left:640px;background:var(--blue)}
  .abs{position:absolute}

  /* brand */
  .brand{display:flex;align-items:center;gap:12px}
  .brand__dot{width:44px;height:44px;border-radius:50%;flex:none}
  .brand__name{font-family:"Roboto Condensed",sans-serif;font-weight:400;font-size:34px;line-height:1.05}
  .brand--front{left:26px;top:44px}
  .brand--front .brand__dot{background:var(--green)}
  .brand--front .brand__name{color:var(--green)}
  .brand--back{left:0;right:0;top:58px;justify-content:center}
  .brand--back .brand__dot{background:var(--white)}
  .brand--back .brand__name{color:var(--white)}

  /* photo areas */
  .photo-hero{left:0;top:0;width:460px;height:450px;background:linear-gradient(180deg,#c6d2e7 0%,#e9dcd6 38%,#d7c9c4 50%,#8c98b2 62%,#6d7890 100%)}
  .photo-bio{left:0;top:480px;width:460px;height:460px;background:linear-gradient(90deg,#a79a8b 0%,#b7aa9a 35%,#cfcac4 55%,#e6e6e6 70%,#ececec 100%)}

  /* front content */
  .title-box{left:37px;top:491px;width:389px;height:90px;border:2px solid var(--blue);border-radius:10px}
  .title-box__kicker{position:absolute;top:-20px;left:50%;transform:translateX(-50%);background:var(--white);padding:0 10px;font-family:"Cinzel",serif;font-size:27px;color:var(--teal-text);white-space:nowrap;letter-spacing:1px}
  .title-box__script{position:absolute;left:0;right:0;top:12px;text-align:center;font-family:"Dancing Script",cursive;font-weight:600;font-size:58px;color:var(--blue-deep);line-height:1}
  .group-name{left:0;right:0;top:598px;text-align:center;font-weight:700;font-size:28px;color:var(--teal-text)}
  .group-leader{left:0;right:0;top:630px;text-align:center;font-size:13px;color:var(--ink)}
  .price-band{left:0;top:665px;width:460px;height:80px;background:var(--grey-band);text-align:center}
  .price-band__weeks{font-family:"Montserrat",sans-serif;font-weight:800;font-size:33px;color:var(--teal-text);line-height:1;margin-top:9px}
  .price-band__cost{font-family:"Montserrat",sans-serif;font-weight:800;font-size:29px;color:var(--blue-deep);line-height:1;margin-top:4px}
  .size-strip{left:0;top:745px;width:460px;height:22px;background:var(--teal);text-align:center;font-size:14px;line-height:22px;color:var(--ink)}
  .topics-head{left:0;right:0;top:778px;text-align:center;font-weight:700;font-size:15px;color:var(--blue-deep)}
  .topics{top:803px;list-style:none;font-size:13.4px;color:var(--ink);line-height:16.8px}
  .topics--left{left:28px}
  .topics--right{left:258px}
  .topics li{display:flex;align-items:center;gap:8px}
  .topics svg{flex:none}
  .topics-divider{left:231px;top:805px;width:1px;height:95px;background:#d8d8d8}

  /* footer */
  .footer-wave{left:0;top:900px;width:460px;height:120px}
  .contact{left:0;right:0;top:946px;text-align:center;color:var(--white)}
  .contact__lead{font-weight:300;font-size:15.5px;line-height:20px}
  .contact__name{font-weight:700;font-size:16.5px;line-height:20px}
  .contact__lines{display:flex;justify-content:center;gap:14px;font-weight:300;font-size:16px;line-height:22px;margin-top:2px}
  .contact__lines span{display:flex;align-items:center;gap:6px}

  /* back content */
  .letter{left:38px;width:384px;color:var(--white);font-weight:300;font-size:15px;line-height:18.6px;text-align:justify;text-align-last:center}
  .letter--one{top:206px}
  .letter--two{top:318px}
  .signoff{left:0;right:0;top:438px;text-align:center;color:var(--white);font-weight:700;font-size:23px}
  .bio-wave{left:0;top:470px;width:460px;height:110px}
  .bio{left:270px;top:618px;width:168px;color:var(--ink);font-weight:700;font-size:14.4px;line-height:18.6px;display:flex;flex-direction:column;gap:18px}
</style>
</head>
<body>

<section class="card card--front" aria-label="Front of rack card">
  <div class="abs photo-hero" role="img" aria-label="Photo of a woman seen from behind, meditating cross-legged on a rock above a calm sea at dusk"></div>
  <div class="abs brand brand--front">
    <span class="brand__dot"></span>
    <span class="brand__name">Still Waters<br>Counseling</span>
  </div>
  <svg class="abs" style="left:0;top:350px" width="460" height="150" viewBox="0 0 460 150" aria-hidden="true">
    <path d="M0 80 Q200 190 460 40 L460 150 L0 150 Z" fill="var(--teal)"/>
    <path d="M0 92 Q205 198 460 55 L460 150 L0 150 Z" fill="var(--blue)"/>
    <path d="M0 100 Q210 190 460 80 L460 150 L0 150 Z" fill="var(--white)"/>
  </svg>

  <div class="abs title-box">
    <div class="title-box__kicker">HEALING THE</div>
    <div class="title-box__script">Hurting Heart</div>
  </div>
  <div class="abs group-name">WOMEN'S TRAUMA &amp; LOSS GROUP</div>
  <div class="abs group-leader">LED BY LICENSED PROFESSIONAL COUNSELOR, JOY BELDEN CRANE</div>

  <div class="abs price-band">
    <div class="price-band__weeks">10 WEEK GROUP</div>
    <div class="price-band__cost">COST - $35 SESSION</div>
  </div>
  <div class="abs size-strip">GROUP SIZE LIMITED TO 10 PARTICIPANTS</div>

  <div class="abs topics-head">TOPICS INCLUDE:</div>
  <ul class="abs topics topics--left">
    <li><svg width="11" height="11" viewBox="0 0 12 12"><circle cx="6" cy="6" r="5" fill="none" stroke="var(--teal)" stroke-width="1.2"/><path d="M3.5 6.2 5.3 8 9.5 3.6" fill="none" stroke="var(--teal)" stroke-width="1.3"/></svg>What is Trauma?</li>
    <li><svg width="11" height="11" viewBox="0 0 12 12"><circle cx="6" cy="6" r="5" fill="none" stroke="var(--teal)" stroke-width="1.2"/><path d="M3.5 6.2 5.3 8 9.5 3.6" fill="none" stroke="var(--teal)" stroke-width="1.3"/></svg>How Trauma Affects Us</li>
    <li><svg width="11" height="11" viewBox="0 0 12 12"><circle cx="6" cy="6" r="5" fill="none" stroke="var(--teal)" stroke-width="1.2"/><path d="M3.5 6.2 5.3 8 9.5 3.6" fill="none" stroke="var(--teal)" stroke-width="1.3"/></svg>Creating a Feeling of Safety</li>
    <li><svg width="11" height="11" viewBox="0 0 12 12"><circle cx="6" cy="6" r="5" fill="none" stroke="var(--teal)" stroke-width="1.2"/><path d="M3.5 6.2 5.3 8 9.5 3.6" fill="none" stroke="var(--teal)" stroke-width="1.3"/></svg>Managing Trauma Triggers</li>
    <li><svg width="11" height="11" viewBox="0 0 12 12"><circle cx="6" cy="6" r="5" fill="none" stroke="var(--teal)" stroke-width="1.2"/><path d="M3.5 6.2 5.3 8 9.5 3.6" fill="none" stroke="var(--teal)" stroke-width="1.3"/></svg>Importance of Self Care</li>
    <li><svg width="11" height="11" viewBox="0 0 12 12"><circle cx="6" cy="6" r="5" fill="none" stroke="var(--teal)" stroke-width="1.2"/><path d="M3.5 6.2 5.3 8 9.5 3.6" fill="none" stroke="var(--teal)" stroke-width="1.3"/></svg>Healthy vs. Unhealthy Coping</li>
  </ul>
  <div class="abs topics-divider"></div>
  <ul class="abs topics topics--right">
    <li><svg width="11" height="11" viewBox="0 0 12 12"><circle cx="6" cy="6" r="5" fill="none" stroke="var(--teal)" stroke-width="1.2"/><path d="M3.5 6.2 5.3 8 9.5 3.6" fill="none" stroke="var(--teal)" stroke-width="1.3"/></svg>Guilt, Shame, and Blame</li>
    <li><svg width="11" height="11" viewBox="0 0 12 12"><circle cx="6" cy="6" r="5" fill="none" stroke="var(--teal)" stroke-width="1.2"/><path d="M3.5 6.2 5.3 8 9.5 3.6" fill="none" stroke="var(--teal)" stroke-width="1.3"/></svg>Victim vs. Victimized</li>
    <li><svg width="11" height="11" viewBox="0 0 12 12"><circle cx="6" cy="6" r="5" fill="none" stroke="var(--teal)" stroke-width="1.2"/><path d="M3.5 6.2 5.3 8 9.5 3.6" fill="none" stroke="var(--teal)" stroke-width="1.3"/></svg>Grieving through Loss</li>
    <li><svg width="11" height="11" viewBox="0 0 12 12"><circle cx="6" cy="6" r="5" fill="none" stroke="var(--teal)" stroke-width="1.2"/><path d="M3.5 6.2 5.3 8 9.5 3.6" fill="none" stroke="var(--teal)" stroke-width="1.3"/></svg>Anger and Forgiveness</li>
    <li><svg width="11" height="11" viewBox="0 0 12 12"><circle cx="6" cy="6" r="5" fill="none" stroke="var(--teal)" stroke-width="1.2"/><path d="M3.5 6.2 5.3 8 9.5 3.6" fill="none" stroke="var(--teal)" stroke-width="1.3"/></svg>Imagining a Better Future</li>
  </ul>

  <svg class="abs footer-wave" viewBox="0 0 460 120" aria-hidden="true">
    <path d="M0 50 Q230 -5 460 45 L460 120 L0 120 Z" fill="var(--teal-light)"/>
    <path d="M0 38 Q220 -2 460 62 L460 120 L0 120 Z" fill="var(--blue)"/>
  </svg>
  <div class="abs contact">
    <div class="contact__lead">For More Information, Contact:</div>
    <div class="contact__name">JOY BELDEN CRANE, LPC, LMFT</div>
    <div class="contact__lines">
      <span><svg width="16" height="16" viewBox="0 0 16 16"><circle cx="8" cy="8" r="8" fill="var(--white)"/><path d="M5.2 4.2c.4-.3.9-.2 1.1.2l.7 1.3c.2.4.1.8-.2 1l-.5.4c.4.9 1.1 1.6 2 2l.4-.5c.3-.3.7-.4 1-.2l1.3.7c.4.2.5.7.2 1.1-.6.8-1.5 1-2.4.6C6.8 10.2 5.3 8.7 4.7 6.7c-.3-.9 0-1.8.5-2.5z" fill="var(--blue)"/></svg>(555) 614-3928</span>
      <span><svg width="16" height="16" viewBox="0 0 16 16"><circle cx="8" cy="8" r="8" fill="var(--white)"/><rect x="4" y="5" width="8" height="6" rx="1" fill="var(--blue)"/><path d="M4.3 5.4 8 8.3l3.7-2.9" fill="none" stroke="var(--white)" stroke-width="1"/></svg>joy@brightmeadowcare.example</span>
    </div>
  </div>
</section>

<section class="card card--back" aria-label="Back of rack card">
  <div class="abs brand brand--back">
    <span class="brand__dot"></span>
    <span class="brand__name">Still Waters<br>Counseling</span>
  </div>

  <p class="abs letter letter--one">Life hurts and does not seem fair. So what do you do when you are faced with an event in your life that knocks you off your feet? It seems no one understands what you are feeling and no one knows just what to say. It is tempting to pull away and isolate or put up a mask and pretend everything is OK.</p>
  <p class="abs letter letter--two">It is my desire you know that you are not alone! There are others who understand the feelings you are going through and offer a safe place for encouraging support. I want to invite you to embark on a courageous journey of healing where you will not only learn how to "survive" after trauma and loss, but instead, learn that you can once again "thrive"!</p>
  <div class="abs signoff">JOY BELDEN CRANE, LPC, LMFT</div>

  <div class="abs photo-bio" role="img" aria-label="Photo of the counselor sitting on a blanket on a rock at the beach, with dunes and a boardwalk behind her"></div>
  <svg class="abs bio-wave" viewBox="0 0 460 110" aria-hidden="true">
    <path d="M0 0 L460 0 L460 90 Q250 -20 0 75 Z" fill="var(--blue)"/>
    <path d="M0 75 Q250 -20 460 90 L460 100 Q250 0 0 90 Z" fill="var(--teal)"/>
    <path d="M0 90 Q250 0 460 100 L460 106 Q250 12 0 98 Z" fill="var(--blue)"/>
  </svg>
  <div class="abs bio">
    <p>Joy Belden Crane is a Licensed Professional Counselor and Licensed Marriage and Family Therapist. She is the owner of Still Waters Counseling Services located in Tulsa, OK.</p>
    <p>Joy is a trauma survivor herself and understands firsthand the unique challenges that can arise on the journey to healing.</p>
  </div>

  <svg class="abs footer-wave" viewBox="0 0 460 120" aria-hidden="true">
    <path d="M0 50 Q230 -5 460 45 L460 120 L0 120 Z" fill="var(--teal-light)"/>
    <path d="M0 38 Q220 -2 460 62 L460 120 L0 120 Z" fill="var(--blue)"/>
  </svg>
  <div class="abs contact">
    <div class="contact__lead">For More Information, Contact:</div>
    <div class="contact__name">JOY BELDEN CRANE, LPC, LMFT</div>
    <div class="contact__lines">
      <span><svg width="16" height="16" viewBox="0 0 16 16"><circle cx="8" cy="8" r="8" fill="var(--white)"/><path d="M5.2 4.2c.4-.3.9-.2 1.1.2l.7 1.3c.2.4.1.8-.2 1l-.5.4c.4.9 1.1 1.6 2 2l.4-.5c.3-.3.7-.4 1-.2l1.3.7c.4.2.5.7.2 1.1-.6.8-1.5 1-2.4.6C6.8 10.2 5.3 8.7 4.7 6.7c-.3-.9 0-1.8.5-2.5z" fill="var(--blue)"/></svg>(555) 614-3928</span>
      <span><svg width="16" height="16" viewBox="0 0 16 16"><circle cx="8" cy="8" r="8" fill="var(--white)"/><rect x="4" y="5" width="8" height="6" rx="1" fill="var(--blue)"/><path d="M4.3 5.4 8 8.3l3.7-2.9" fill="none" stroke="var(--white)" stroke-width="1"/></svg>joy@brightmeadowcare.example</span>
    </div>
  </div>
</section>

</body>
</html>
```